BrightGable.net
Professional
Hal Pemberly
President
718 Quillmoor Rd.
Calder Springs, GA 30418
hpemberly@brightgable.net
www.brightgable.net
The logo file actually has 2 versions of our logo on it. One with the symbol on the left side of the name and one with the symbol above the name. I did this so that when you are designing the business card you can pick which ever one works best with your design. I also have ones with various other changes (i.e. without the lines) if anyone needs them.

```html
<!DOCTYPE html>
<html lang="en">
<head>
<meta charset="utf-8">
<title>BrightGable.net Stationery</title>
<link href="https://fonts.googleapis.com/css2?family=Open+Sans:wght@400;600;700&display=swap" rel="stylesheet">
<style>
:root{
  --board:#3a3a3c;
  --paper:#ffffff;
  --ink:#4a4a4a;
  --ink-soft:#7a7a7a;
  --brand:#1d5f9e;
  --brand-bright:#1fa6e8;
  --navy:#061a4a;
}
*{box-sizing:border-box;margin:0;padding:0}
html,body{width:1200px;height:796px;overflow:hidden}
body{background:var(--board);font-family:"Open Sans",Arial,sans-serif;color:var(--ink);position:relative}

.piece{position:absolute;background:var(--paper);box-shadow:0 2px 8px rgba(0,0,0,.45)}

/* brand lockup */
.brand{display:flex;align-items:center;gap:8px}
.brand-dot{border-radius:50%;background:var(--brand-bright);flex:none}
.brand-text{display:flex;flex-direction:column;line-height:1}
.brand-host{font-size:7px;font-weight:700;color:var(--brand);letter-spacing:.5px}
.brand-name{font-weight:700;color:var(--brand);letter-spacing:-.3px}
.brand-tag{font-size:5.5px;font-weight:700;color:var(--brand);letter-spacing:.6px;margin-top:2px}

/* letterhead */
.letterhead{left:29px;top:29px;width:511px;height:744px;padding:34px 40px}
.letterhead .brand-dot{width:30px;height:30px}
.letterhead .brand-name{font-size:22px}
.letter-body{margin-top:36px;font-size:9.5px;line-height:1.55;color:var(--ink-soft);width:430px}
.letter-body p{margin-bottom:14px}
.letter-sign{margin-top:26px}
.letter-company{font-size:7.5px;letter-spacing:.4px;margin-top:12px}
.letter-foot{position:absolute;right:44px;bottom:30px;display:flex;font-size:9.5px;line-height:1.4;color:var(--ink)}
.letter-foot .col{padding:0 10px}
.letter-foot .col+.col{border-left:1px solid #999}

/* cards */
.card-contact{left:163px;top:228px;width:264px;height:160px;padding:12px 14px}
.card-contact .brand-dot{width:18px;height:18px}
.card-contact .brand-name{font-size:13px}
.card-contact .brand-host{font-size:5px}
.card-name{position:absolute;left:14px;top:50px;font-size:12px;color:var(--brand)}
.card-role{position:absolute;left:14px;top:68px;font-size:7px}
.card-addr{position:absolute;left:150px;top:20px;font-size:6.5px;line-height:1.4}
.card-reach{position:absolute;left:150px;top:50px;font-size:6.5px;line-height:1.4}
.card-front{left:290px;top:300px;width:250px;height:150px;background:radial-gradient(ellipse at 60% 45%,var(--brand-bright),#0a58b5 55%,var(--navy));display:flex;align-items:center;justify-content:flex-end;padding-right:16px}
.card-front .brand{gap:6px}
.card-front .brand-dot{width:20px;height:20px;background:#ffffff}
.card-front .brand-name{font-size:14px;color:#ffffff}
.card-front .brand-host{font-size:5px;color:#ffffff}
.card-logo{left:168px;top:345px;width:190px;height:130px;display:flex;align-items:center;justify-content:center}
.card-logo .brand{flex-direction:column;gap:6px}
.card-logo .brand-dot{width:30px;height:30px}
.card-logo .brand-name{font-size:13px}

/* envelopes */
.envelope{left:569px;width:612px;overflow:hidden}
.envelope svg.flap{position:absolute;left:0;top:0}
.envelope-top{top:29px;height:379px}
.envelope-bottom{top:420px;height:353px}
.envelope .brand{position:absolute;left:26px;top:150px}
.envelope .brand-dot{width:30px;height:30px}
.envelope .brand-name{font-size:22px}
.env-address{position:absolute;font-size:10px;line-height:1.35;color:var(--ink)}
.envelope-top .env-address{right:32px;top:268px;display:flex;gap:36px}
.envelope-bottom .env-address{right:32px;top:310px}
</style>
</head>
<body>

<section class="piece letterhead">
  <div class="brand">
    <span class="brand-dot"></span>
    <div class="brand-text">
      <span class="brand-host">CLOUD TOOLS FOR TEAMS</span>
      <span class="brand-name">BrightGable.net</span>
      <span class="brand-tag">YOUR OFFICE, WHEREVER YOU ARE</span>
    </div>
  </div>
  <div class="letter-body">
    <p>March 02, 2011</p>
    <p>Lorem ipsum dolor sit amet, consectetur adipiscing elit. Donec nec ligula sed urna ullamcorper pretium. Nullam sit amet justo in lectus feugiat fermentum. Integer vitae magna eu erat porta pulvinar sed non lorem.</p>
    <p>Mauris ut lorem vel nisi luctus gravida. Aliquam erat volutpat. Curabitur a dui eget massa tempus dignissim. Vivamus commodo lacus non orci ultrices, at placerat neque venenatis.</p>
    <p>Nullam egestas tincidunt lacus, vitae blandit turpis consequat in. Sed eleifend mattis nunc, quis dapibus magna rhoncus eget. Phasellus sed leo vel neque aliquet semper.</p>
    <p>Etiam a magna nec diam pulvinar fringilla fermentum nec magna. Quisque dictum dolor sit amet lorem sagittis id dignissim nisi luctus. Fusce vehicula cursus purus.</p>
    <p class="letter-sign">Sincerely yours,</p>
    <p class="letter-company">YOUR BIG CORPORATE</p>
  </div>
  <div class="letter-foot">
    <div class="col">P: 612-555-0182<br>F: 612-555-0147</div>
    <div class="col">718 Quillmoor Rd.<br>Calder Springs, GA 30418</div>
  </div>
</section>

<section class="piece card-contact">
  <div class="brand">
    <span class="brand-dot"></span>
    <div class="brand-text">
      <span class="brand-host">CLOUD TOOLS FOR TEAMS</span>
      <span class="brand-name">BrightGable.net</span>
    </div>
  </div>
  <div class="card-addr">718 Quillmoor Rd.<br>Calder Springs, GA 30418</div>
  <div class="card-reach">P: 612-555-0182<br>F: 612-555-0147<br>hpemberly@brightgable.net<br>www.brightgable.net</div>
  <div class="card-name">Hal Pemberly</div>
  <div class="card-role">President</div>
</section>

<section class="piece card-front">
  <div class="brand">
    <span class="brand-dot"></span>
    <div class="brand-text">
      <span class="brand-host">CLOUD TOOLS FOR TEAMS</span>
      <span class="brand-name">BrightGable.net</span>
    </div>
  </div>
</section>

<section class="piece card-logo">
  <div class="brand">
    <span class="brand-dot"></span>
    <span class="brand-name">BrightGable.net</span>
  </div>
</section>

<section class="piece envelope envelope-top">
  <svg class="flap" width="612" height="130" viewBox="0 0 612 130" aria-hidden="true">
    <defs>
      <linearGradient id="flapTop" x1="0" y1="0" x2="0" y2="1">
        <stop offset="0" stop-color="#061a4a"/>
        <stop offset=".35" stop-color="#0b3fa0"/>
        <stop offset="1" stop-color="#1fa6e8"/>
      </linearGradient>
    </defs>
    <path d="M0 0H612V40Q600 75 560 88L330 118Q306 122 282 118L52 88Q12 75 0 40Z" fill="url(#flapTop)"/>
  </svg>
  <div class="brand">
    <span class="brand-dot"></span>
    <div class="brand-text">
      <span class="brand-host">CLOUD TOOLS FOR TEAMS</span>
      <span class="brand-name">BrightGable.net</span>
      <span class="brand-tag">YOUR OFFICE, WHEREVER YOU ARE</span>
    </div>
  </div>
  <div class="env-address">
    <div>718 Quillmoor Rd.<br>Calder Springs, GA 30418</div>
    <div>P: 612-555-0182<br>F: 612-555-0147</div>
  </div>
</section>

<section class="piece envelope envelope-bottom">
  <svg class="flap" width="612" height="140" viewBox="0 0 612 140" aria-hidden="true">
    <defs>
      <linearGradient id="flapBottom" x1="0" y1="0" x2="0" y2="1">
        <stop offset="0" stop-color="#061a4a"/>
        <stop offset=".4" stop-color="#0b3fa0"/>
        <stop offset="1" stop-color="#1fa6e8"/>
      </linearGradient>
    </defs>
    <path d="M0 0H612V38Q520 44 420 70L320 128Q306 136 292 128L192 70Q92 44 0 38Z" fill="url(#flapBottom)"/>
  </svg>
  <div class="brand">
    <span class="brand-dot"></span>
    <div class="brand-text">
      <span class="brand-host">CLOUD TOOLS FOR TEAMS</span>
      <span class="brand-name">BrightGable.net</span>
      <span class="brand-tag">YOUR OFFICE, WHEREVER YOU ARE</span>
    </div>
  </div>
  <div class="env-address">718 Quillmoor Rd. Calder Springs, GA 30418</div>
</section>

</body>
</html>
```